Tessellaria

Club flyer, grand opening night, house/electronic music, looking for clean design with a sample image attached. Please look at the prior flyers to get an idea of the style. Guaranteed project
I would like to use the red design if possible (tessellaria flyer attached)
Text:
TESSELLARIA
Winter House Music Monthly
Opening Night Dec 13 2013
Pellmont (use logo)
Featuring
BRAMOX (House/Garage)
(use logo with just Bramox name)
w/ resident
ORV (Driftwerk)
Free All Night
21-39 year old club with all house/electronic music. classier and grown up over gimmicky
Club

```html
<!DOCTYPE html>
<html lang="en">
<head>
<meta charset="utf-8">
<title>Tessellaria – Winter House Music Monthly</title>
<link rel="stylesheet" href="https://fonts.googleapis.com/css2?family=Poiret+One&family=Marcellus&family=Oswald:wght@500;600&display=swap">
<style>
  :root {
    --red-warm: #d0503a;
    --red: #b3302a;
    --red-deep: #761915;
    --charcoal: #1c1a1a;
    --night: #050505;
    --gold: #c9a074;
    --gold-light: #f3e3cf;
    --silver: #e9e9ea;
  }
  html, body {
    margin: 0;
    padding: 0;
    overflow: hidden;
    background: #000;
  }
  .flyer {
    position: relative;
    width: 1200px;
    height: 1000px;
    overflow: hidden;
    font-family: "Oswald", sans-serif;
  }
  .backdrop {
    position: absolute;
    inset: 0;
    background: linear-gradient(110deg, var(--red-warm) 0%, var(--red) 28%, var(--red-deep) 52%, var(--charcoal) 72%, var(--night) 100%);
  }
  .title {
    position: absolute;
    top: 62px;
    left: 0;
    width: 1130px;
    margin: 0;
    text-align: center;
    font-family: "Poiret One", sans-serif;
    font-weight: 400;
    font-size: 104px;
    letter-spacing: 6px;
    color: var(--gold);
    text-shadow: 0 0 1px var(--gold-light);
  }
  .subtitle {
    position: absolute;
    top: 198px;
    left: 0;
    width: 1100px;
    margin: 0;
    text-align: center;
    font-family: "Oswald", sans-serif;
    font-weight: 500;
    font-size: 42px;
    line-height: 64px;
    color: var(--silver);
    text-shadow: 2px 2px 3px #000;
  }
  .offer {
    position: absolute;
    top: 500px;
    left: 0;
    width: 1140px;
    margin: 0;
    text-align: center;
    font-family: "Marcellus", serif;
    font-weight: 400;
    font-size: 88px;
    color: var(--gold);
  }
  .venue {
    position: absolute;
    left: 57px;
    top: 740px;
    display: flex;
    align-items: center;
    gap: 12px;
    font-family: "Marcellus", serif;
    font-size: 40px;
    color: var(--silver);
  }
  .venue__mark {
    width: 24px;
    height: 24px;
    background: var(--silver);
  }
  .resident {
    position: absolute;
    left: 38px;
    top: 830px;
    margin: 0;
    font-family: "Oswald", sans-serif;
    font-weight: 600;
    color: #fff;
    text-shadow: 2px 2px 3px #000;
  }
  .resident__label {
    display: block;
    margin-left: 4px;
    font-size: 42px;
    line-height: 60px;
  }
  .resident__name {
    display: block;
    font-size: 38px;
    line-height: 66px;
  }
  .guest {
    position: absolute;
    right: 30px;
    top: 842px;
    width: 220px;
    margin: 0;
    text-align: center;
  }
  .guest__label {
    display: block;
    font-family: "Marcellus", serif;
    font-size: 32px;
    color: #fff;
  }
  .guest__name {
    display: block;
    margin-top: 12px;
    font-family: "Marcellus", serif;
    font-size: 50px;
    letter-spacing: 1px;
    color: var(--silver);
  }
</style>
</head>
<body>
<main class="flyer">
  <div class="backdrop" role="img" aria-label="Abstract backdrop artwork in red fading to black"></div>

  <h1 class="title">TESSELLARIA</h1>
  <p class="subtitle">Winter House Music Monthly<br>Opening Night Dec 13 2013</p>

  <p class="offer">FREE ALL NIGHT</p>

  <div class="venue"><span class="venue__mark"></span>Pellmont</div>

  <p class="resident">
    <span class="resident__label">w/ resident</span>
    <span class="resident__name">ORV (Driftwerk)</span>
  </p>

  <p class="guest">
    <span class="guest__label">FEATURING</span>
    <span class="guest__name">BRAMOX</span>
  </p>
</main>
</body>
</html>
```